Letterhead Design Project

Based on the attached logo we would like have a designed of stationary.
As we are a management consulting company focused on business development dealing with C-level and one level below we new business cards.
We have decided to use HGP (Harbor Growth Partners) as the business name. The legal name will be Harbor Growth Partners ApS but we will brand us under HGP. The tack line is “Shaping Steady Gains” if we need one.
For legal reasons we need to have the legal name on the letters together with the company no. (cvr. nr. 58197024)
We want to signal the following:
- Serious
- Professional
- Creating Result
- Capable of thinking out of the box and creative
- Fast reactions we will be there when needed
What we do not want to be view as is:
- To smart
- We know better
- We can fix it yesterday
Our Value Proposition is two sited:
- Increasing revenue
- Reduced sales cost or increased efficiency
Therefore, companies can call us when they want to grow or they need to be more efficient.
Our business cards should have a two sided print with the logo incl. the tack line on one side and the detailed information on the other site.
We need to have the following information on the letter head:
- Legal company name
- Cvr nr.
- Address incl. country name (Denmark)
- Main number
- Wed address
Symbols are welcome to be used to guide for the above information.
The following information are expected to be in the personal signature of the letter.
- Name
- Title
- Mobile number
- E-mail address
Updates
Some of you has requested our specific details so here they come:
- Address incl. country name (Denmark): Lyngvejen 42, 3460 Birkerød, Denmark
- Main number: +45 5871 3302
- Wed address: www.klmrises.example
Mobile no. are +45 xxxx xxxx or +45 4390 1256
Our e-mail looks like this: firstname.seconname@KLMRISES.EXAMPLE or for me: jonas.halvorsen@klmrises.example
We need the design (file) as finish as posible so we just need to add personal details before printing.
Please be aware that we will prefer designs where we can print the full letter incl. design. As we are communicating on e-mails with pdf versions of the letter we also need to have a design which will print on the clients printers.
Target Market(s)
C level and one level below.
Major local and international Companies.
Industry/Entity Type
Management Consulting
Font styles to use
Colors
Designer to choose colors to be used in the design.
Requirements
Must have
- Use of our logo without tack line

```html
<!DOCTYPE html>
<html lang="en">
<head>
<meta charset="utf-8">
<title>HGP Stationery</title>
<link href="https://fonts.googleapis.com/css2?family=Fira+Sans:wght@400;500;700&display=swap" rel="stylesheet">
<style>
:root{
  --stage:#a4a4a1;
  --paper:#ffffff;
  --brand:#1462b3;
  --brand-dark:#0b4f9c;
  --ink:#3a3a3a;
  --band:#e3ecf6;
  --band-lilac:#e6e3ef;
  --grey-light:#f4f4f4;
  --grey-mid:#b9b9b9;
  --card-lilac:#a9b5e0;
}
*{margin:0;padding:0;box-sizing:border-box}
html,body{width:1200px;height:1000px;overflow:hidden}
body{background:var(--stage);font-family:"Fira Sans",Arial,sans-serif;position:relative}
.sheet{position:absolute;background:var(--paper);border:1px solid #555;overflow:hidden}
.sheet svg.deco{position:absolute;inset:0;width:100%;height:100%}
.wordmark{position:absolute;font-family:"Fira Sans",Arial,sans-serif;font-weight:700;color:var(--brand);letter-spacing:-1px;line-height:1}

/* letterhead */
.letterhead{left:96px;top:35px;width:494px;height:710px}
.letterhead .wordmark{left:24px;top:24px;font-size:38px}
.letterhead .tagline{position:absolute;right:26px;top:21px;font-size:13px;color:var(--brand)}
.letterhead .footer{position:absolute;left:0;right:0;bottom:11px;display:flex;justify-content:center;gap:18px;font-size:11px;color:var(--ink);letter-spacing:.3px;white-space:nowrap}
.letterhead .footer .dot{color:var(--brand)}

/* business card back */
.card-back{left:627px;top:180px;width:307px;height:176px}
.card-back .wordmark{left:20px;top:18px;font-size:34px}
.card-back .person{position:absolute;right:8px;top:56px;text-align:right;color:#fff}
.card-back .person .name{font-size:14px;line-height:1.1}
.card-back .person .role{font-size:10px}
.card-back .contacts{position:absolute;left:26px;top:105px;list-style:none;font-size:11.5px;color:var(--ink)}
.card-back .contacts li{display:flex;align-items:center;gap:9px;height:15.5px}
.card-back .contacts svg{width:11px;height:11px;flex:none}

/* business card front */
.card-front{left:826px;top:34px;width:308px;height:176px;background:radial-gradient(ellipse at 50% 45%,#ffffff 0%,#dfe4f5 35%,var(--card-lilac) 100%)}
.card-front .wordmark{left:0;right:0;top:28px;text-align:center;font-size:56px}
.card-front .tagline{position:absolute;left:0;right:0;top:126px;text-align:center;font-size:17px;color:var(--brand-dark)}

/* envelope */
.envelope{left:551px;top:385px;width:609px;height:301px}
.envelope .sender{position:absolute;left:45px;top:23px;font-size:11px;line-height:16px;color:var(--brand-dark)}
.envelope .sender .legal{font-weight:500}
.envelope .wordmark{left:46px;top:198px;font-size:44px}
.envelope .tagline{position:absolute;left:49px;top:261px;font-size:12px;color:var(--brand-dark)}
.envelope .window{position:absolute;left:366px;top:191px;width:190px;height:82px;border:1px solid #cfcfcf;border-radius:12px;background:#fff;display:flex;align-items:center;justify-content:center;font-size:11px;color:var(--brand-dark)}
</style>
</head>
<body>

<section class="sheet letterhead">
  <svg class="deco" viewBox="0 0 494 710" preserveAspectRatio="none" aria-hidden="true">
    <path d="M0,0 H494 V112 C400,140 250,142 0,86 Z" fill="var(--band)"/>
    <polygon points="170,0 262,0 445,128 320,134" fill="var(--band-lilac)" opacity=".7"/>
  </svg>
  <div class="wordmark">HGP</div>
  <div class="tagline">Shaping Steady Gains</div>
  <div class="footer">
    <span>Lyngvejen 42, 3460 Birkerød</span><span class="dot">•</span>
    <span>www.hgprises.example</span><span class="dot">•</span>
    <span>+45 4390 1256</span>
  </div>
</section>

<section class="sheet card-front">
  <div class="wordmark">HGP</div>
  <div class="tagline">Shaping Steady Gains</div>
</section>

<section class="sheet card-back">
  <svg class="deco" viewBox="0 0 307 176" preserveAspectRatio="none" aria-hidden="true">
    <defs>
      <linearGradient id="cardGrey" x1="0" y1="0" x2="0" y2="1">
        <stop offset="0" stop-color="var(--grey-light)"/>
        <stop offset="1" stop-color="var(--grey-mid)"/>
      </linearGradient>
    </defs>
    <path d="M0,122 C60,72 150,56 307,54 V176 H0 Z" fill="url(#cardGrey)"/>
    <path d="M158,56 C205,48 265,44 307,42 V103 C245,103 195,86 158,56 Z" fill="var(--brand-dark)"/>
  </svg>
  <div class="wordmark">HGP</div>
  <div class="person">
    <div class="name">Name Person</div>
    <div class="role">President</div>
  </div>
  <ul class="contacts">
    <li><svg viewBox="0 0 12 12"><rect x="3" y="0.5" width="6" height="11" rx="1" fill="none" stroke="var(--brand-dark)" stroke-width="1.3"/><rect x="4.5" y="2" width="3" height="6" fill="var(--brand-dark)"/></svg>+45 5871 3302</li>
    <li><svg viewBox="0 0 12 12"><rect x="0.7" y="2.5" width="10.6" height="7.5" fill="none" stroke="var(--brand-dark)" stroke-width="1.2"/><path d="M0.7,2.5 L6,7 L11.3,2.5" fill="none" stroke="var(--brand-dark)" stroke-width="1.2"/></svg>name@hgprises.example</li>
    <li><svg viewBox="0 0 12 12"><rect x="1.5" y="1.5" width="9" height="6.5" fill="none" stroke="var(--brand-dark)" stroke-width="1.2"/><rect x="0" y="9.5" width="12" height="1.5" fill="var(--brand-dark)"/></svg>www.hgprises.example</li>
    <li><svg viewBox="0 0 12 12"><path d="M6,11.5 C3,7.5 2.5,6 2.5,4.5 A3.5,3.5 0 0 1 9.5,4.5 C9.5,6 9,7.5 6,11.5 Z" fill="var(--brand-dark)"/><circle cx="6" cy="4.5" r="1.3" fill="#fff"/></svg>Anywhere, Denmark</li>
  </ul>
</section>

<section class="sheet envelope">
  <svg class="deco" viewBox="0 0 609 301" preserveAspectRatio="none" aria-hidden="true">
    <defs>
      <linearGradient id="envGrey" x1="0" y1="0" x2="1" y2="0">
        <stop offset="0" stop-color="#d2d2d2"/>
        <stop offset=".5" stop-color="#a9a9a9"/>
        <stop offset="1" stop-color="#f0f0f0"/>
      </linearGradient>
    </defs>
    <polygon points="384,162 560,140 609,200 609,301 472,301" fill="url(#envGrey)"/>
    <path d="M0,0 H609 V128 C480,162 260,178 0,108 Z" fill="var(--band)"/>
    <polygon points="300,0 400,0 600,132 470,155" fill="var(--band-lilac)" opacity=".7"/>
  </svg>
  <div class="sender">
    <div class="legal">Harbor Growth Partners ApS</div>
    <div>+45 5871 3302</div>
    <div>cvr. nr. 58197024</div>
    <div>Anywhere, Denmark</div>
    <div>www.hgprises.example</div>
  </div>
  <div class="wordmark">HGP</div>
  <div class="tagline">Shaping Steady Gains</div>
  <div class="window">John Doe</div>
</section>

</body>
</html>
```